Party planning business card design

Galas with Wren is a party planning business

Function Planning: Weddings/Themed Parties/Children's Parties

Adult and Children's Photo Booths
Party Themed boxes,
We can find the venue, entertainment. face painters.

Children's costumes and accessories - Sell / Hire

Web: www.galaswithwren.example
Facebook: Galas with Wren

Industry/Entity Type

Party Planning

Contact Information for Business Card

Galas With Wren, Rosalind Pektrew,
Creative Director

Colors
e34297
000000

Requirements
Must have
• on my logo are you able to edit the stars to pink?

```html
<!DOCTYPE html>
<html lang="en">
<head>
<meta charset="utf-8">
<title>Galas with Wren – Business Card</title>
<link href="https://fonts.googleapis.com/css2?family=Lato:wght@400;700;900&family=Quicksand:wght@500;700&display=swap" rel="stylesheet">
<style>
  :root {
    --pink: #e34297;
    --pink-deep: #c8307f;
    --warm: #f07a4a;
    --ink: #111111;
    --grey: #3a3a3a;
    --paper: #ffffff;
    --backdrop: #2b2b2d;
  }
  * { margin: 0; padding: 0; box-sizing: border-box; }
  html, body {
    width: 1200px; height: 900px; overflow: hidden;
    background: var(--backdrop);
    font-family: "Lato", Arial, sans-serif;
  }

  /* ---------- back of card ---------- */
  .card-back {
    position: absolute; left: 40px; top: 40px;
    width: 600px; height: 343px;
    border-radius: 24px; overflow: hidden;
    background: var(--pink);
  }
  .card-back__photo {
    position: absolute; left: 0; top: 0; width: 100%; height: 200px;
    background: linear-gradient(180deg, var(--warm) 0%, #e8608a 55%, var(--pink) 100%);
  }
  .card-back__brand {
    position: absolute; left: 0; right: 0; top: 196px; text-align: center;
    font-family: "Quicksand", "Lato", sans-serif;
    font-size: 38px; font-weight: 700; color: var(--paper); letter-spacing: 2px;
  }
  .card-back__rule {
    position: absolute; left: 110px; right: 110px; top: 252px;
    height: 2px; background: var(--ink); opacity: .7;
  }
  .card-back__tagline {
    position: absolute; left: 0; right: 0; top: 264px; text-align: center;
    font-family: "Quicksand", "Lato", sans-serif;
    font-size: 28px; font-weight: 700; color: var(--ink); letter-spacing: 1.5px;
  }

  /* ---------- front of card ---------- */
  .card {
    position: absolute; left: 400px; top: 426px;
    width: 760px; height: 434px;
    border-radius: 28px; overflow: hidden;
    background: var(--paper);
  }
  .card__shapes { position: absolute; inset: 0; }
  .logo {
    position: absolute; left: 50px; top: 120px;
    display: flex; align-items: center; gap: 14px;
  }
  .logo__dot { width: 26px; height: 26px; border-radius: 50%; background: var(--pink); flex: none; }
  .logo__name { font-size: 30px; font-weight: 700; color: var(--grey); letter-spacing: 1px; }
  .identity { position: absolute; right: 62px; top: 40px; text-align: right; }
  .identity__name { font-size: 26px; font-weight: 900; color: var(--pink); letter-spacing: 1px; line-height: 1.1; }
  .identity__role { font-size: 15px; font-weight: 700; color: var(--ink); margin-top: 2px; }
  .contacts { position: absolute; right: 34px; top: 104px; list-style: none; }
  .contacts li {
    display: flex; justify-content: flex-end; align-items: center; gap: 12px;
    font-size: 16px; font-weight: 700; color: var(--ink); height: 30px;
  }
  .contacts .accent { color: var(--pink); }
  .contacts svg { width: 18px; height: 18px; fill: var(--pink); flex: none; }
  .services {
    position: absolute; top: 268px;
    font-size: 16px; font-weight: 700; color: var(--paper);
    text-transform: uppercase; line-height: 1.35; letter-spacing: .4px;
  }
  .services--left { left: 70px; }
  .services--right { right: 40px; text-align: center; }
  .functions {
    position: absolute; left: 0; right: 0; top: 350px;
    display: flex; justify-content: center; align-items: center; gap: 12px;
    font-size: 20px; font-weight: 700; color: var(--ink); text-transform: uppercase;
  }
  .functions__divider { width: 4px; height: 24px; background: var(--pink); }
</style>
</head>
<body>
  <section class="card-back">
    <div class="card-back__photo" role="img" aria-label="Photo of guests celebrating at a party"></div>
    <p class="card-back__brand">Galas with Wren</p>
    <div class="card-back__rule"></div>
    <p class="card-back__tagline">We get the Party Started</p>
  </section>

  <article class="card">
    <svg class="card__shapes" viewBox="0 0 760 434" aria-hidden="true">
      <path fill="var(--pink)" d="M0,0 H600 C560,0 555,26 515,26 H0 Z"/>
      <rect fill="var(--pink)" x="0" y="256" width="760" height="82"/>
      <path fill="var(--pink)" d="M210,434 C250,434 250,398 300,398 H760 V434 Z"/>
    </svg>

    <div class="logo" role="img" aria-label="Galas with Wren logo">
      <span class="logo__dot"></span>
      <span class="logo__name">Galas with Wren</span>
    </div>

    <header class="identity">
      <h1 class="identity__name">ROSALIND</h1>
      <p class="identity__role">Creative Director</p>
    </header>

    <ul class="contacts">
      <li>Marlow Bay, Queensland, Australia 4999
        <svg viewBox="0 0 24 24"><path d="M12 3 2 12h3v9h5v-6h4v6h5v-9h3z"/></svg></li>
      <li>0491570156
        <svg viewBox="0 0 24 24"><path d="M6.6 10.8a15 15 0 0 0 6.6 6.6l2.2-2.2a1 1 0 0 1 1-.25 11.4 11.4 0 0 0 3.6.57 1 1 0 0 1 1 1V20a1 1 0 0 1-1 1A17 17 0 0 1 3 4a1 1 0 0 1 1-1h3.5a1 1 0 0 1 1 1c0 1.25.2 2.45.57 3.6a1 1 0 0 1-.25 1z"/></svg></li>
      <li>rosalind@galaswithwren.example
        <svg viewBox="0 0 24 24"><path d="M2 5h20v14H2zm2 2v.5l8 5 8-5V7l-8 5z"/></svg></li>
      <li><span>www.<span class="accent">galaswithwren.example</span></span>
        <svg viewBox="0 0 24 24"><circle cx="12" cy="12" r="10"/><circle cx="12" cy="12" r="5" fill="#fff"/></svg></li>
    </ul>

    <p class="services services--left">Adult &amp; Children's Photo<br>Booths &amp; Party Themed Boxes</p>
    <p class="services services--right">We can find the venue,<br>entertainment. face painters.</p>

    <p class="functions">
      <span>Weddings</span><span class="functions__divider"></span>
      <span>Themed Parties</span><span class="functions__divider"></span>
      <span>Children's Parties</span>
    </p>
  </article>
</body>
</html>
```